High Quality fast food restaurant - Tomanyo

Tomanyo is a fast food company with its target's focused on logistic, simplicity, high quality, freshness and modern.

We need a web design where the customers can get a complete idea of our high quality completeness, we want to take fast food to a new upper level.

We would like to see the colours of wood and metal. Pictures have been attached of our local.

We would like to have something in similar to: http://www.qpz.example/
Updates

Images for the food we are going to sell can be found here: http://shrt.example/uWQa7

It will be the images with rice, french fries or pita bread.

Target Market(s)

The fast food eating people between sloppy food and restaurant level.

Industry/Entity Type

Fast Food Restaurant

Requirements
Should not have
• No Flash or Java

```html
<!DOCTYPE html>
<html lang="en">
<head>
<meta charset="utf-8">
<title>Tomanyo – High Quality Fast Food</title>
<link href="https://fonts.googleapis.com/css2?family=Lobster&family=Oswald:wght@500;600&display=swap" rel="stylesheet">
<style>
  :root {
    --brown-dark: #2d160e;
    --brown-wood: #3a1f15;
    --red-top: #ef3b43;
    --red-bottom: #c0141b;
    --red-edge: #a50f15;
    --yellow: #f5e21a;
    --fold: #e8b21a;
    --white: #ffffff;
  }
  html, body {
    margin: 0;
    padding: 0;
    overflow: hidden;
    background: var(--brown-dark);
  }
  .page {
    position: relative;
    width: 1200px;
    height: 900px;
    overflow: hidden;
    background: var(--brown-dark);
    font-family: "Oswald", sans-serif;
  }
  .hero {
    position: absolute;
    left: 0; top: 0;
    width: 1200px; height: 567px;
    background:
      radial-gradient(circle at 10% 35%, #b8231c 0, transparent 22%),
      radial-gradient(circle at 30% 10%, #c0391e 0, transparent 18%),
      radial-gradient(circle at 88% 45%, #4e7a2a 0, transparent 20%),
      radial-gradient(circle at 80% 85%, #a8261a 0, transparent 22%),
      radial-gradient(circle at 15% 85%, #6b4426 0, transparent 25%),
      linear-gradient(180deg, #6a3a24 0%, #8a4a2a 50%, #5a3320 100%);
  }
  .hero-panel {
    position: absolute;
    left: 225px; top: 0;
    width: 750px; height: 567px;
    background: rgba(255, 240, 225, 0.28);
  }
  .hero-food {
    position: absolute;
    left: 255px; top: 140px;
    width: 705px; height: 427px;
    border-radius: 40px 40px 0 0;
    background:
      radial-gradient(ellipse at 80% 55%, #9a4a22 0, transparent 45%),
      radial-gradient(ellipse at 35% 70%, #f0b540 0, transparent 40%),
      radial-gradient(ellipse at 38% 25%, #d61f26 0, transparent 35%),
      linear-gradient(180deg, #e9d2b5, #e3b07a);
  }
  .headline {
    position: absolute;
    left: 0; width: 1200px; top: 74px;
    margin: 0;
    text-align: center;
    font-family: "Lobster", cursive;
    font-weight: 400;
    font-size: 40px;
    color: var(--yellow);
    text-shadow: 2px 2px 3px rgba(0,0,0,0.45);
  }
  .topnav {
    position: absolute;
    top: 17px;
    height: 41px;
    display: flex;
    background: linear-gradient(180deg, var(--red-top), var(--red-bottom));
    box-shadow: 0 2px 4px rgba(0,0,0,0.4);
  }
  .topnav.left { left: 208px; width: 245px; }
  .topnav.right { left: 740px; width: 251px; }
  .topnav a {
    display: flex;
    align-items: center;
    justify-content: center;
    color: var(--white);
    text-decoration: none;
    font-weight: 600;
    font-size: 16px;
    border-right: 1px solid rgba(255,255,255,0.35);
  }
  .topnav a:last-child { border-right: none; }
  .fold {
    position: absolute;
    top: 58px;
    width: 0; height: 0;
    border-top: 12px solid var(--fold);
  }
  .fold.left { left: 208px; border-left: 17px solid transparent; }
  .fold.right { left: 975px; border-right: 17px solid transparent; }
  .brand {
    position: absolute;
    left: 453px; top: 0;
    width: 287px; height: 76px;
    background: linear-gradient(180deg, var(--brown-wood), #2a140c);
    display: flex;
    align-items: center;
    justify-content: center;
    color: var(--white);
    font-weight: 600;
    font-size: 28px;
    letter-spacing: 1px;
  }
  .promo {
    position: absolute;
    top: 575px;
    height: 173px;
    background: linear-gradient(180deg, var(--red-top), var(--red-bottom));
    border-bottom: 2px solid var(--red-edge);
    box-shadow: 0 3px 6px rgba(0,0,0,0.45);
  }
  .promo.special { left: 225px; width: 369px; }
  .promo.offers { left: 603px; width: 372px; }
  .promo-photo {
    position: absolute;
    left: 19px; top: 26px;
    width: 146px; height: 120px;
    background: var(--white);
  }
  .promo-photo span {
    position: absolute;
    inset: 6px;
    display: block;
  }
  .special .promo-photo span { background: radial-gradient(ellipse at 50% 55%, #8a4a22 0, #d9a05a 45%, #ffffff 75%); }
  .offers .promo-photo span { background: radial-gradient(ellipse at 50% 60%, #9a6a3a 0, #e6c79a 45%, #ffffff 78%); }
  .promo-title {
    position: absolute;
    left: 178px; right: 0; top: 28px;
    margin: 0;
    text-align: center;
    font-family: "Lobster", cursive;
    font-weight: 400;
    font-size: 42px;
    line-height: 49px;
    color: var(--white);
    text-shadow: 2px 2px 3px rgba(0,0,0,0.4);
  }
  .footer-nav {
    position: absolute;
    top: 797px; left: 0; width: 1200px;
    display: flex;
    justify-content: center;
    gap: 0;
  }
  .footer-nav a {
    color: var(--white);
    text-decoration: none;
    font-weight: 600;
    font-size: 14px;
    padding: 0 22px;
  }
  .footer-nav .sep { color: var(--white); font-size: 14px; }
  .footer-text {
    position: absolute;
    top: 826px; left: 330px; width: 540px;
    margin: 0;
    text-align: center;
    font-family: Arial, Helvetica, sans-serif;
    font-size: 9.5px;
    line-height: 12px;
    color: var(--white);
  }
</style>
</head>
<body>
<div class="page">
  <div class="hero" role="img" aria-label="Blurred background photo of burgers and fast food"></div>
  <div class="hero-panel"></div>
  <div class="hero-food" role="img" aria-label="Photo of a double cheeseburger, french fries and a red soft drink cup"></div>
  <h1 class="headline">High Quality Fast Food</h1>

  <nav class="topnav left">
    <a href="#" style="width:103px">Menu</a>
    <a href="#" style="width:142px">Today Special</a>
  </nav>
  <div class="fold left"></div>
  <div class="brand">TOMANYO</div>
  <nav class="topnav right">
    <a href="#" style="width:102px">Deliver</a>
    <a href="#" style="width:149px">Contact Us</a>
  </nav>
  <div class="fold right"></div>

  <section class="promo special">
    <div class="promo-photo"><span role="img" aria-label="Photo of a cheeseburger"></span></div>
    <h2 class="promo-title">Today<br>Special</h2>
  </section>
  <section class="promo offers">
    <div class="promo-photo"><span role="img" aria-label="Photo of pita bread wraps in a basket"></span></div>
    <h2 class="promo-title">View<br>Offers</h2>
  </section>

  <nav class="footer-nav">
    <a href="#">Menu</a><span class="sep">|</span>
    <a href="#">Today Special</a><span class="sep">|</span>
    <a href="#">Our Offers</a><span class="sep">|</span>
    <a href="#">Deliver</a><span class="sep">|</span>
    <a href="#">Contact Us</a>
  </nav>
  <p class="footer-text">Duis autem vel eum iriure dolor in hendrerit in vulputate velit esse molestie consequat, vel illum dolore eu feugiat nulla facilisis at vero eros et accumsan et iusto odio dignissim qui blandit praesent luptatum zzril delenit augue duis dolore te feugait nulla facilisi.</p>
</div>
</body>
</html>
```